Need a website for our company

We need a website for our company to showcase all our work for customers to see.
We do all phases of home improvement:
Dormers/Extensions
Basement Remodel
Masonry/Concrete/Pavers/Asphalt
Cultured Stone Veneer
Kitchens
Bathrooms
Pool designs
Outdoor Bathroom
Outdoor Kitchens
Tile work
For reference, something similar to this website: https://brightlanebuilders.example/
Target Market(s)
We are trying to target homeowners.
Coding
Coded - Design and coding required
Number of Pages Required
5+ page
Look and feel

```html
<!DOCTYPE html>
<html lang="en">
<head>
<meta charset="utf-8">
<title>Bright Lane Builders — Home Extension &amp; Renovation</title>
<link href="https://fonts.googleapis.com/css2?family=Barlow+Condensed:wght@500;600;700&family=Montserrat:wght@400;500;600&family=Dancing+Script:wght@600&display=swap" rel="stylesheet">
<style>
:root{
  --black:#111111;
  --ink:#1c1c1c;
  --text:#3a3a3a;
  --muted:#6b6b6b;
  --grey:#d9d9d9;
  --tab:#e6e6e6;
  --tab-active:#5a5a5a;
  --icon-bg:#c9c9c9;
  --social:#4a4a4a;
  --accent:#e8541c;
  --white:#ffffff;
}
*{margin:0;padding:0;box-sizing:border-box}
html,body{width:1200px;height:4292px;overflow:hidden}
body{position:relative;background:var(--white);font-family:"Montserrat",sans-serif;color:var(--ink)}
.abs{position:absolute}
.center{left:0;width:1200px;text-align:center}
.script{font-family:"Dancing Script",cursive;font-size:34px;color:var(--muted);line-height:1}
.title{font-family:"Montserrat",sans-serif;font-weight:400;font-size:34px;line-height:1;color:var(--ink)}
.btn{position:absolute;background:var(--black);color:var(--white);border-radius:30px;display:flex;align-items:center;justify-content:center;gap:10px;font-size:19px;font-weight:500;letter-spacing:.5px;white-space:nowrap}

/* hero */
.hero{top:0;left:0;width:1200px;height:620px}
.hero-photo{position:absolute;inset:0;background:linear-gradient(180deg,#6e7780 0%,#5c5147 40%,#4d5a33 75%,#3b4a24 100%)}
.hero-shade{position:absolute;inset:0;background:rgba(0,0,0,.28)}
.brand{position:absolute;left:25px;top:0;width:122px;height:103px;background:var(--black);color:var(--white);display:flex;align-items:center;justify-content:center;text-align:center;font-family:"Montserrat",sans-serif;font-weight:600;font-size:15px;line-height:1.25}
.call{position:absolute;left:950px;top:8px;width:225px;height:42px;background:var(--black);border-radius:21px;color:var(--white);display:flex;align-items:center;gap:10px;padding-left:26px}
.call small{display:block;font-size:11px}
.call b{display:block;font-size:18px;font-weight:600;line-height:1}
.nav{position:absolute;top:64px;left:0;width:1200px;font-size:14px;font-weight:600;color:var(--white)}
.nav span{position:absolute;transform:translateX(-50%);white-space:nowrap}
.hero h1{position:absolute;top:182px;left:0;width:1200px;text-align:center;font-family:"Barlow Condensed",sans-serif;font-weight:700;font-size:54px;line-height:66px;letter-spacing:2px;color:var(--white)}

/* about */
.stat{position:absolute;top:1068px;width:160px;height:75px;border:1px solid #bbb;box-shadow:0 2px 4px rgba(0,0,0,.25);text-align:center;padding-top:9px}
.stat b{display:block;font-weight:400;font-size:26px}
.stat small{font-size:12px;color:var(--text)}

/* services */
.svc{position:absolute;width:200px;text-align:center}
.svc .ring{width:134px;height:134px;margin:0 auto;border:4px solid var(--black);border-radius:50%;background:var(--icon-bg);display:flex;align-items:center;justify-content:center}
.svc h3{font-family:"Barlow Condensed",sans-serif;font-weight:700;font-size:16px;margin-top:6px;line-height:1.1}
.svc p{font-size:12px;color:var(--text);line-height:1.25;margin-top:5px}
.svc a{font-size:12px;color:var(--accent);text-decoration:none;display:block;margin-top:3px}

/* projects */
.tabs{position:absolute;left:0;width:1200px;display:flex;justify-content:center;gap:18px}
.tabs span{background:var(--tab);font-size:17px;padding:4px 12px;color:var(--text);white-space:nowrap}
.tabs .active{background:var(--tab-active);color:var(--white)}
.card{position:absolute;top:2910px;width:275px;height:273px}
.card .cap{position:absolute;bottom:0;left:0;width:100%;height:37px;background:rgba(20,20,20,.85);color:var(--white);font-size:17px;text-align:center;line-height:37px}

/* why */
.feature{position:absolute;top:3600px;display:flex;gap:12px}
.feature h4{font-weight:500;font-size:17px;line-height:1.1}
.feature p{font-size:13px;color:var(--text);line-height:1.2;margin-top:2px}
.divider{position:absolute;top:3592px;width:1px;height:116px;background:#999}

/* footer */
.foot{color:var(--white)}
.foot h5{font-weight:500;font-size:17px}
.foot li{list-style:none;font-size:13px;position:absolute;white-space:nowrap}
.social{position:absolute;top:4155px;width:52px;height:48px;background:var(--social)}
</style>
</head>
<body>

<!-- Hero -->
<header class="abs hero">
  <div class="hero-photo" role="img" aria-label="Photo of a smiling family sitting on the lawn in front of a brick house"></div>
  <div class="hero-shade"></div>
  <svg class="abs" style="left:0;top:480px" width="1200" height="140" viewBox="0 0 1200 140">
    <path d="M0 20 Q600 190 1200 20 L1200 140 L0 140Z" fill="#111"/>
    <path d="M0 45 Q600 170 1200 20 L1200 140 L0 140Z" fill="#fff"/>
  </svg>
  <div class="brand">Bright Lane<br>Builders</div>
  <div class="call">
    <svg width="24" height="24" viewBox="0 0 24 24"><path d="M6 2l4 5-2 3c1 3 3 5 6 6l3-2 5 4-3 4C10 21 3 14 2 5z" fill="#fff"/></svg>
    <div><small>Call Us</small><b>(555) 010-4567</b></div>
  </div>
  <nav class="nav">
    <span style="left:597px">HOME</span><span style="left:713px">ABOUT US</span><span style="left:843px">SERVICES</span><span style="left:978px">OUR WORK</span><span style="left:1125px">CONTACT US</span>
  </nav>
  <h1>EXPERIENCED AND TRUSTED HOME<br>EXTENSION AND RENOVATION<br>BUILDERS</h1>
  <div class="btn" style="left:438px;top:430px;width:324px;height:44px">GET YOUR FREE&nbsp; ESTIMATE</div>
</header>

<!-- About -->
<section>
  <div class="abs script" style="left:217px;top:686px;width:200px;text-align:center">About Us</div>
  <div class="abs title" style="left:117px;top:723px;width:400px;text-align:center">Who We Are</div>
  <p class="abs" style="left:35px;top:828px;width:555px;font-size:13.5px;line-height:20px;color:var(--text)">Lorem ipsum dolor sit amet, consectetur adipiscing elit, sed do eiusmod tempor incididunt ut labore et dolore magna aliqua. Quis ipsum suspendisse ultrices gravida. Risus commodo viverra maecenas accumsan lacus vel facilisis.</p>
  <div class="btn" style="left:185px;top:947px;width:243px;height:43px">MORE ABOUT US
    <svg width="30" height="12" viewBox="0 0 30 12"><path d="M0 6h28M22 1l6 5-6 5" stroke="#fff" stroke-width="1.6" fill="none"/></svg></div>
  <div class="stat" style="left:37px"><b>30</b><small>Years of Experience</small></div>
  <div class="stat" style="left:228px"><b>12k+</b><small>Projects Completed</small></div>
  <div class="stat" style="left:422px"><b>10k+</b><small>Happy Clients</small></div>
  <div class="abs" style="left:661px;top:695px;width:494px;height:494px;border-radius:50%;background:var(--black)"></div>
  <div class="abs" role="img" aria-label="Photo of a two-storey suburban house with a covered porch" style="left:675px;top:709px;width:466px;height:466px;border-radius:50%;background:radial-gradient(circle at 50% 40%,#c9b8a0,#8d7a64 60%,#5e5244)"></div>
</section>

<!-- Services -->
<section>
  <div class="abs script center" style="top:1268px">Our Service</div>
  <div class="abs title center" style="top:1302px">What We Do</div>

  <div class="svc" style="left:33px;top:1355px"><div class="ring"><svg width="80" height="60" viewBox="0 0 80 60"><path d="M5 35L40 8l35 27" stroke="#333" stroke-width="5" fill="none"/><rect x="16" y="32" width="48" height="22" fill="#333"/><rect x="28" y="38" width="10" height="10" fill="#c9c9c9"/><rect x="46" y="38" width="10" height="10" fill="#c9c9c9"/></svg></div><h3>DORMERS/EXTENSIONS</h3><p>Lorem ipsum dolor sit amet, consectetur ...</p><a>Learn More ⟶</a></div>
  <div class="svc" style="left:270px;top:1355px"><div class="ring"><svg width="70" height="70" viewBox="0 0 70 70"><path d="M8 62V30L35 8l27 22v32z M20 62V44h12v-8h12v-8" stroke="#333" stroke-width="4" fill="none"/></svg></div><h3>BASEMENT REMODEL</h3><p>Lorem ipsum dolor sit amet, consectetur ...</p><a>Learn More ⟶</a></div>
  <div class="svc" style="left:503px;top:1355px"><div class="ring"><svg width="70" height="60" viewBox="0 0 70 60" fill="#333"><rect x="4" y="8" width="28" height="12"/><rect x="38" y="8" width="28" height="12"/><rect x="4" y="24" width="14" height="12"/><rect x="22" y="24" width="26" height="12"/><rect x="52" y="24" width="14" height="12"/><rect x="4" y="40" width="28" height="12"/><rect x="38" y="40" width="28" height="12"/></svg></div><h3>MASONRY/CONCRETE/<br>PAVERS/ASPHALT</h3><p>Lorem ipsum dolor sit amet, consectetur ...</p><a>Learn More ⟶</a></div>
  <div class="svc" style="left:737px;top:1355px"><div class="ring"><svg width="66" height="66" viewBox="0 0 66 66" fill="#333"><path d="M4 4h26l-4 22H4z M34 4h28v16l-24 6z M4 30h20l4 32H4z M30 30l32-6v18H32z M32 46h30v16H34z"/></svg></div><h3>CULTURED STONE VENEER</h3><p>Lorem ipsum dolor sit amet, consectetur ...</p><a>Learn More ⟶</a></div>
  <div class="svc" style="left:970px;top:1355px"><div class="ring"><svg width="76" height="66" viewBox="0 0 76 66" fill="none" stroke="#333" stroke-width="4"><rect x="4" y="24" width="68" height="38"/><path d="M4 38h68M36 24v38M30 4h16v10H30z M26 18h24"/></svg></div><h3>KITCHENS</h3><p>Lorem ipsum dolor sit amet, consectetur ...</p><a>Learn More ⟶</a></div>

  <div class="svc" style="left:33px;top:1630px"><div class="ring"><svg width="76" height="66" viewBox="0 0 76 66" fill="#333"><rect x="4" y="26" width="68" height="36" rx="4"/><rect x="10" y="40" width="56" height="3" fill="#c9c9c9"/><path d="M36 26V8h12v6" stroke="#333" stroke-width="4" fill="none"/></svg></div><h3>BATHROOMS</h3><p>Lorem ipsum dolor sit amet, consectetur ...</p><a>Learn More ⟶</a></div>
  <div class="svc" style="left:270px;top:1630px"><div class="ring"><svg width="70" height="66" viewBox="0 0 70 66" fill="none" stroke="#333" stroke-width="4"><path d="M20 44V10a6 6 0 0 1 12 0M40 44V10a6 6 0 0 1 12 0M20 22h20M20 34h20M4 52q8-6 16 0t16 0 16 0 14 0M4 62q8-6 16 0t16 0 16 0 14 0"/></svg></div><h3>POOL DESIGNS</h3><p>Lorem ipsum dolor sit amet, consectetur ...</p><a>Learn More ⟶</a></div>
  <div class="svc" style="left:503px;top:1630px"><div class="ring"><svg width="76" height="66" viewBox="0 0 76 66"><path d="M6 30h64v10a20 20 0 0 1-20 20H26A20 20 0 0 1 6 40z" fill="#333"/><path d="M14 30V10a6 6 0 0 1 12 0v4" stroke="#333" stroke-width="4" fill="none"/></svg></div><h3>OUTDOOR BATHROOM</h3><p>Lorem ipsum dolor sit amet, consectetur ...</p><a>Learn More ⟶</a></div>
  <div class="svc" style="left:737px;top:1630px"><div class="ring"><svg width="66" height="70" viewBox="0 0 66 70" fill="none" stroke="#333" stroke-width="4"><path d="M6 18h54a27 27 0 0 1-54 0z M22 40l-10 26M44 40l10 26M33 44v18"/><circle cx="14" cy="62" r="4"/></svg></div><h3>OUTDOOR KITCHENS</h3><p>Lorem ipsum dolor sit amet, consectetur ...</p><a>Learn More ⟶</a></div>
  <div class="svc" style="left:970px;top:1630px"><div class="ring"><svg width="76" height="76" viewBox="0 0 76 76" fill="#333"><path d="M38 4l14 14-14 14-14-14z M18 24l14 14-14 14L4 38z M58 24l14 14-14 14-14-14z M38 44l14 14-14 14-14-14z"/></svg></div><h3>TILE WORK</h3><p>Lorem ipsum dolor sit amet, consectetur ...</p><a>Learn More ⟶</a></div>

  <div class="btn" style="left:438px;top:1880px;width:324px;height:47px">VIEW ALL SERVICES</div>
</section>

<!-- Before / After -->
<section>
  <svg class="abs" style="left:0;top:2008px" width="1200" height="600" viewBox="0 0 1200 600" role="img" aria-label="Dark interior room backdrop with plants and chairs">
    <defs><linearGradient id="room" x1="0" y1="0" x2="1" y2="0"><stop offset="0" stop-color="#2a2a2a"/><stop offset=".5" stop-color="#1a1a1a"/><stop offset="1" stop-color="#2c2c2c"/></linearGradient></defs>
    <path d="M0 90 Q600 -40 1200 90 L1200 500 Q600 620 0 500Z" fill="url(#room)"/>
  </svg>
  <div class="abs" style="left:288px;top:2112px;width:624px;height:380px;border:3px solid #ddd;display:flex">
    <div role="img" aria-label="Room under renovation with stripped walls, before photo" style="flex:1;background:linear-gradient(180deg,#6b5a45,#4a4036 60%,#7d7a72);position:relative"><span style="position:absolute;bottom:40px;left:0;width:100%;text-align:center;font-size:30px;color:#111">Before</span></div>
    <div role="img" aria-label="Renovated bright room with wooden floor, after photo" style="flex:1;background:linear-gradient(180deg,#e9e9e6,#d4d2cc 60%,#b77a3c);position:relative"><span style="position:absolute;bottom:40px;left:0;width:100%;text-align:center;font-size:30px;color:#111">After</span></div>
  </div>
  <svg class="abs" style="left:118px;top:2265px" width="74" height="74" viewBox="0 0 74 74"><circle cx="37" cy="37" r="37" fill="#0a0a0a"/><path d="M43 23L29 37l14 14" stroke="#fff" stroke-width="6" fill="none" stroke-linecap="round"/></svg>
  <svg class="abs" style="left:1006px;top:2265px" width="74" height="74" viewBox="0 0 74 74"><circle cx="37" cy="37" r="37" fill="#0a0a0a"/><path d="M31 23l14 14-14 14" stroke="#fff" stroke-width="6" fill="none" stroke-linecap="round"/></svg>
</section>

<!-- Projects -->
<section>
  <div class="abs script center" style="top:2685px">Feauture Projects</div>
  <div class="abs title center" style="top:2720px">Our Projects</div>
  <div class="tabs" style="top:2792px"><span class="active">Dormers/Extensions</span><span>Basement Remodel</span><span>Masonry/Concrete/Pavers/Asphalt</span><span>Cultured Stone Veneer</span></div>
  <div class="tabs" style="top:2838px"><span>Kitchens</span><span>Bathrooms</span><span>Pool designs</span><span>Outdoor Bathroom</span><span>Outdoor Kitchens</span><span>Tile work</span></div>
  <div class="card" style="left:25px;background:linear-gradient(160deg,#3f7fd6,#d7dce2 55%,#c4532a)" role="img" aria-label="Photo of a white dormer on a red tile roof"><div class="cap">Project Name</div></div>
  <div class="card" style="left:317px;background:linear-gradient(180deg,#9fc1e6,#7a4a3a 50%,#4d6b35)" role="img" aria-label="Photo of a large brick house with front lawn"><div class="cap">Project Name</div></div>
  <div class="card" style="left:608px;background:linear-gradient(150deg,#c98a66,#8a5a42 50%,#3d3d3d)" role="img" aria-label="Photo of a copper-clad dormer on a slate roof"><div class="cap">Project Name</div></div>
  <div class="card" style="left:900px;background:linear-gradient(180deg,#7fb0e6,#e8e8e8 45%,#b8502c)" role="img" aria-label="Photo of a dormer window on a red tiled roof"><div class="cap">Project Name</div></div>
  <div class="btn" style="left:458px;top:3220px;width:284px;height:45px">VIEW ALL PROJECTS
    <svg width="30" height="12" viewBox="0 0 30 12"><path d="M0 6h28M22 1l6 5-6 5" stroke="#fff" stroke-width="1.6" fill="none"/></svg></div>
</section>

<!-- Why choose us -->
<section>
  <div class="abs script center" style="top:3412px">Why Like Us</div>
  <div class="abs title center" style="top:3456px">Why Choose Us</div>
  <p class="abs center" style="top:3500px;font-size:15px;line-height:21px;color:var(--text)">There are many Variations of passages of Lorem Ipsum abailable, But the<br>Majority have suffered alteration.</p>

  <div class="feature" style="left:110px">
    <svg width="52" height="48" viewBox="0 0 52 48" fill="none" stroke="#333" stroke-width="2.5"><path d="M26 44L6 24a11 11 0 0 1 20-14 11 11 0 0 1 20 14z"/></svg>
    <div style="width:210px"><h4>We Care</h4><p>Lorem ipsum dolor sit amet, consectetur adipiscing elit, sed do eiusmod tempor incididunt ut labore et dolore magna</p></div>
  </div>
  <div class="divider" style="left:418px"></div>
  <div class="feature" style="left:468px">
    <svg width="52" height="52" viewBox="0 0 52 52" fill="none" stroke="#333" stroke-width="2.5"><rect x="4" y="8" width="40" height="38" rx="3"/><path d="M4 18h40M14 4v8M34 4v8"/><circle cx="38" cy="40" r="10" fill="#fff"/><path d="M38 34v6l4 3"/></svg>
    <div style="width:210px"><h4>Customer Service with<br>Extened Hour</h4><p>Lorem ipsum dolor sit amet, consectetur adipiscing elit, sed do eiusmod tempor incididunt</p></div>
  </div>
  <div class="divider" style="left:777px"></div>
  <div class="feature" style="left:828px">
    <svg width="48" height="52" viewBox="0 0 48 52" fill="none" stroke="#333" stroke-width="2.5"><path d="M6 12l10-8h16l10 8v36H6z M18 4v44M30 4v44M6 30h36"/></svg>
    <div style="width:210px"><h4>Safety Matters</h4><p>Lorem ipsum dolor sit amet, consectetur adipiscing elit, sed do eiusmod tempor incididunt</p></div>
  </div>
</section>

<!-- Footer -->
<footer class="foot">
  <svg class="abs" style="left:0;top:3890px" width="1200" height="402" viewBox="0 0 1200 402"><path d="M0 95 Q600 -20 1200 95 L1200 402 L0 402Z" fill="#111"/></svg>
  <div class="abs" style="left:263px;top:3733px;width:682px;height:250px;background:var(--grey);box-shadow:0 3px 8px rgba(0,0,0,.3);text-align:center;color:var(--ink)">
    <div style="margin-top:70px;font-size:25px">For Project Queries Call to Us at</div>
    <div style="margin-top:28px;font-size:54px;font-weight:500;display:flex;justify-content:center;align-items:center;gap:14px;white-space:nowrap">
      <svg width="50" height="50" viewBox="0 0 24 24"><path d="M6 2l4 5-2 3c1 3 3 5 6 6l3-2 5 4-3 4C10 21 3 14 2 5z" fill="none" stroke="#111" stroke-width="1.6"/></svg>(555) 010-0199</div>
  </div>

  <div class="abs" style="left:45px;top:4060px;font-size:24px;font-weight:600;line-height:1.2;color:var(--white)">Bright Lane<br>Builders</div>
  <div class="social" style="left:43px" role="img" aria-label="Social profile link"></div>
  <div class="social" style="left:103px" role="img" aria-label="Messaging link"></div>
  <div class="social" style="left:163px" role="img" aria-label="Social feed link"></div>

  <h5 class="abs" style="left:527px;top:4037px">MENU</h5>
  <ul>
    <li style="left:530px;top:4074px">HOME</li><li style="left:530px;top:4104px">ABOUT US</li><li style="left:530px;top:4135px">SERVICES</li><li style="left:530px;top:4165px">OUR WORK</li><li style="left:530px;top:4197px">CONTACT US</li>
  </ul>

  <h5 class="abs" style="left:917px;top:4037px">PHYSICAL ADDRESS:</h5>
  <svg class="abs" style="left:917px;top:4075px" width="18" height="24" viewBox="0 0 18 24"><path d="M9 0a9 9 0 0 1 9 9c0 6-9 15-9 15S0 15 0 9a9 9 0 0 1 9-9z" fill="#ccc"/><circle cx="9" cy="9" r="3" fill="#111"/></svg>
  <div class="abs" style="left:948px;top:4074px;font-size:13px;line-height:19px">Lorem ipsum dolor sit amet,<br>consectetur adipiscing</div>
  <svg class="abs" style="left:920px;top:4134px" width="18" height="18" viewBox="0 0 24 24"><path d="M6 2l4 5-2 3c1 3 3 5 6 6l3-2 5 4-3 4C10 21 3 14 2 5z" fill="#ccc"/></svg>
  <div class="abs" style="left:948px;top:4135px;font-size:13px">(555) 010-0142</div>
  <svg class="abs" style="left:917px;top:4182px" width="22" height="16" viewBox="0 0 22 16"><rect width="22" height="16" fill="#ccc"/><path d="M0 0l11 9 11-9" stroke="#111" stroke-width="1.5" fill="none"/></svg>
  <div class="abs" style="left:946px;top:4180px;font-size:13px;white-space:nowrap">info@brightlanebuilders.example</div>

  <div class="abs center" style="top:4254px;font-size:14px;color:#666">© 2023 Bright Lane Builders</div>
</footer>

</body>
</html>
```